LUXE Example Spa

We'd like a business card with the reverse of the card for appointments. We like round corners and vertical design. We have a background image and bird logo to include with the following wording on the front:-
Luxe Medical Spa
248 Pemberton Street
NORTH ADELAIDE
SA 5006
Phone 08 84391576
www.luxemedicalspa-example.com.au
Facebook luxeexamplespa
Instagram luxeexamplespa
On the back I'd like an appointment card layout please.
Cheers Dot

```html
<!DOCTYPE html>
<html lang="en">
<head>
<meta charset="utf-8">
<title>Luxe Example Spa – Business and Appointment Card</title>
<link rel="stylesheet" href="https://fonts.googleapis.com/css2?family=Cormorant+Garamond:wght@500&family=Lora:wght@400;600&display=swap">
<style>
  :root {
    --stage: #e6e6e6;
    --mint-top: #a6e0c6;
    --mint-mid: #a2dcc3;
    --teal-low: #7fc7c2;
    --panel: rgba(240, 249, 245, 0.82);
    --ink: #1f2a2a;
    --white: #ffffff;
    --rule: rgba(255, 255, 255, 0.55);
    --line: #b9e0d4;
    --connector: #2d4a48;
  }
  * { box-sizing: border-box; margin: 0; padding: 0; }
  html, body { width: 1200px; height: 900px; overflow: hidden; }
  body {
    background: var(--stage);
    font-family: "Lora", Georgia, serif;
    color: var(--ink);
    position: relative;
  }
  .card {
    position: absolute;
    top: 162px;
    width: 348px;
    height: 576px;
    border-radius: 20px;
    overflow: hidden;
    background: linear-gradient(180deg, var(--mint-top) 0%, var(--mint-mid) 55%, var(--teal-low) 100%);
  }
  .card--appointment { left: 226px; }
  .card--contact { left: 626px; }
  .card__rule {
    position: absolute; left: 0; right: 0; top: 54px;
    height: 1px; background: var(--rule);
  }
  .card__foliage {
    position: absolute; left: 0; right: 0; bottom: 0; height: 62%;
    background:
      radial-gradient(ellipse 70% 55% at 30% 75%, rgba(110, 190, 190, 0.45), transparent 70%),
      radial-gradient(ellipse 60% 45% at 80% 55%, rgba(190, 235, 220, 0.45), transparent 70%);
  }
  .brand {
    position: absolute; left: 0; right: 0;
    text-align: center;
    font-family: "Cormorant Garamond", Georgia, serif;
    font-weight: 500;
    color: var(--white);
    letter-spacing: 0.08em;
    white-space: nowrap;
  }
  .card--appointment .brand { top: 118px; font-size: 30px; }
  .card--contact .brand { top: 212px; font-size: 34px; }

  .appointment {
    position: absolute; left: 16px; top: 206px;
    width: 316px; height: 317px;
    border-radius: 22px;
    background: var(--panel);
  }
  .appointment__title {
    position: absolute; top: 24px; left: 0; right: 0;
    text-align: center; font-weight: 600; font-size: 18px;
  }
  .field-label { position: absolute; left: 30px; font-size: 14px; }
  .field-line { position: absolute; left: 16px; width: 284px; height: 10px; }
  .days {
    position: absolute; left: 38px; top: 120px;
    display: grid; grid-template-columns: repeat(3, 86px); row-gap: 19px;
    font-size: 14px;
  }
  .day { display: flex; align-items: center; gap: 9px; }
  .day__box { width: 27px; height: 16px; border: 1.3px solid var(--ink); }

  .contact-icons {
    position: absolute; top: 352px; left: 0; right: 0;
    display: flex; justify-content: center; align-items: center; gap: 10px;
  }
  .contact-block {
    position: absolute; left: 0; right: 0; text-align: center;
    font-size: 15px; line-height: 22px; font-style: normal;
  }
  .contact-block--reach { top: 379px; }
  .contact-block--address { top: 469px; line-height: 21px; }

  .social {
    position: absolute; left: 0; right: 0; top: 538px;
    display: flex; justify-content: center; align-items: center; gap: 10px;
    color: var(--white); font-size: 14px;
  }
  .social__dot { width: 12px; height: 12px; border-radius: 50%; background: var(--white); }
</style>
</head>
<body>

<section class="card card--appointment" aria-label="Appointment side">
  <div class="card__foliage" role="img" aria-label="Soft palm leaf background"></div>
  <div class="card__rule"></div>
  <div class="brand">LUXE Example Spa</div>

  <div class="appointment">
    <h2 class="appointment__title">Your Next Appointment:</h2>

    <span class="field-label" style="top:70px">Name:</span>
    <svg class="field-line" style="top:88px" viewBox="0 0 284 10"><line x1="4" y1="5" x2="280" y2="5" stroke="#b9e0d4" stroke-width="1.5"/><circle cx="4" cy="5" r="3" fill="#fff" stroke="#b9e0d4"/><circle cx="280" cy="5" r="3" fill="#fff" stroke="#b9e0d4"/></svg>

    <div class="days">
      <label class="day"><span class="day__box"></span>Mon</label>
      <label class="day"><span class="day__box"></span>Tue</label>
      <label class="day"><span class="day__box"></span>Wed</label>
      <label class="day"><span class="day__box"></span>Thu</label>
      <label class="day"><span class="day__box"></span>Fri</label>
      <label class="day"><span class="day__box"></span>Sat</label>
    </div>

    <span class="field-label" style="top:212px">Dated:</span>
    <svg class="field-line" style="top:230px" viewBox="0 0 284 10"><line x1="4" y1="5" x2="280" y2="5" stroke="#b9e0d4" stroke-width="1.5"/><circle cx="4" cy="5" r="3" fill="#fff" stroke="#b9e0d4"/><circle cx="280" cy="5" r="3" fill="#fff" stroke="#b9e0d4"/></svg>

    <span class="field-label" style="top:256px">Time:</span>
    <svg class="field-line" style="top:274px" viewBox="0 0 284 10"><line x1="4" y1="5" x2="280" y2="5" stroke="#b9e0d4" stroke-width="1.5"/><circle cx="4" cy="5" r="3" fill="#fff" stroke="#b9e0d4"/><circle cx="280" cy="5" r="3" fill="#fff" stroke="#b9e0d4"/></svg>
  </div>

  <div class="social">
    <svg width="36" height="6" viewBox="0 0 36 6"><circle cx="3" cy="3" r="2" fill="none" stroke="#2d4a48"/><line x1="5" y1="3" x2="36" y2="3" stroke="#2d4a48"/></svg>
    <span class="social__dot"></span>
    <span>luxeexamplespa</span>
    <svg width="36" height="6" viewBox="0 0 36 6"><line x1="0" y1="3" x2="31" y2="3" stroke="#2d4a48"/><circle cx="33" cy="3" r="2" fill="none" stroke="#2d4a48"/></svg>
  </div>
</section>

<section class="card card--contact" aria-label="Contact side">
  <div class="card__foliage" role="img" aria-label="Soft palm leaf background"></div>
  <div class="card__rule"></div>
  <div class="brand">LUXE Example Spa</div>

  <div class="contact-icons">
    <svg width="46" height="6" viewBox="0 0 46 6"><circle cx="3" cy="3" r="2" fill="none" stroke="#2d4a48"/><line x1="5" y1="3" x2="46" y2="3" stroke="#2d4a48"/></svg>
    <svg width="20" height="18" viewBox="0 0 20 18" aria-label="Phone"><path d="M1 6 Q10 -1 19 6 L16 8 L14 5 Q10 3.5 6 5 L4 8 Z" fill="#fff"/><rect x="4" y="9" width="12" height="8" rx="1.5" fill="#fff"/></svg>
    <svg width="18" height="18" viewBox="0 0 18 18" aria-label="Website"><g fill="none" stroke="#fff" stroke-width="1.4"><circle cx="9" cy="9" r="8"/><ellipse cx="9" cy="9" rx="3.5" ry="8"/><line x1="1" y1="9" x2="17" y2="9"/><line x1="2.5" y1="5" x2="15.5" y2="5"/><line x1="2.5" y1="13" x2="15.5" y2="13"/></g></svg>
    <svg width="46" height="6" viewBox="0 0 46 6"><line x1="0" y1="3" x2="41" y2="3" stroke="#2d4a48"/><circle cx="43" cy="3" r="2" fill="none" stroke="#2d4a48"/></svg>
  </div>

  <div class="contact-block contact-block--reach">
    <p>00 5550 0199</p>
    <p>www.luxemedicalspa-example.com.au</p>
  </div>

  <address class="contact-block contact-block--address">
    <p>248 Pemberton Street</p>
    <p>Fernhaven Vale XA 0000</p>
  </address>

  <div class="social">
    <svg width="36" height="6" viewBox="0 0 36 6"><circle cx="3" cy="3" r="2" fill="none" stroke="#2d4a48"/><line x1="5" y1="3" x2="36" y2="3" stroke="#2d4a48"/></svg>
    <span class="social__dot"></span>
    <span>luxeexamplespa</span>
    <svg width="36" height="6" viewBox="0 0 36 6"><line x1="0" y1="3" x2="31" y2="3" stroke="#2d4a48"/><circle cx="33" cy="3" r="2" fill="none" stroke="#2d4a48"/></svg>
  </div>
</section>

</body>
</html>
```